Brindle-Oak.com -> We need someone to design a homepage [For Mobile]

We need a graphic design of our homepage for mobile, which will include login and signup. It's only the design we need, we would take care of the coding, so if you're a good designer you're welcome to participate. The Login & Registration page contain a few fields. Login --> Username & Password & Forgot my Password. Registration --> Email, Username, Password. Needs to be a clean design.[Registration in a different page, Login and Homepage in the same one]
Updates

Project Deadline Extended Reason: We're going to consider what we got so far and allow others to submit more designs as well, the final deadline would be this week, we won't extend it again. Added Saturday, December 20, 2014

Project Deadline Extended Reason: Very sorry, we just got more than expected designs and we want to go over all of them in order to make a proper decision - we would extend the project until the 1st of January 2015, this is definitely a FINAL date. Added Friday, December 26, 2014

Industry/Entity Type

Graphic Design

Number of Pages Required

2 page

Requirements
Must have
• * Enclosed our logo to include with the design.
• * Add the following text as well
• WANT TO EARN EXTRA MONEY?
• WITH BRINDLE-OAK.COM YOU CAN!
• BRINDLE-OAK.COM. IT'S AS EASY AS 1, 2, 3.
• (1) Register (2) Earn & Win Coins (3) Redeem Coins
• * It must have "Login" and "Register" buttons on the home page.
Nice to have
• [Note: Also to make it easier for you, enclosed a screenshot of the main page in a desktop (PC) view.]

```html
<!DOCTYPE html>
<html lang="en">
<head>
<meta charset="utf-8">
<title>Brindle-Oak – Home</title>
<link href="https://fonts.googleapis.com/css2?family=Figtree:wght@400;500;600;700&display=swap" rel="stylesheet">
<style>
  :root {
    --stage: #455a60;
    --panel: #e6e6e6;
    --green: #72a534;
    --ink: #44545a;
    --muted: #6d7679;
    --placeholder: #b5b5b5;
    --white: #ffffff;
    --mark: #56656a;
  }
  * { box-sizing: border-box; margin: 0; padding: 0; }
  html, body {
    width: 1200px; height: 927px; overflow: hidden;
    background: var(--stage);
    font-family: "Figtree", Arial, sans-serif;
  }
  .screen {
    position: absolute; left: 298px; top: 26px;
    width: 604px; height: 874px;
    background: var(--panel);
  }
  .brand {
    position: absolute; left: 0; right: 0; top: 36px;
    display: flex; align-items: center; justify-content: center; gap: 20px;
  }
  .brand-dot {
    width: 92px; height: 92px; border-radius: 50%;
    background: var(--mark);
  }
  .brand-name {
    font-size: 52px; font-weight: 500; color: var(--ink);
    letter-spacing: -0.5px;
  }
  .pitch {
    position: absolute; left: 0; right: 0; top: 152px;
    text-align: center;
  }
  .pitch-headline {
    font-size: 30px; font-weight: 700; color: var(--green);
    line-height: 38px;
  }
  .pitch-sub {
    font-size: 22px; font-weight: 600; color: var(--ink);
    line-height: 30px; letter-spacing: 0.3px;
  }
  .login-title {
    position: absolute; left: 46px; top: 250px;
    font-size: 34px; font-weight: 600; color: var(--ink);
  }
  .field {
    position: absolute; left: 44px; width: 513px; height: 88px;
    background: var(--white);
    border: 3px solid var(--green); border-radius: 4px;
    padding-left: 16px;
    display: flex; align-items: center;
    font-size: 32px; color: var(--placeholder);
  }
  .field-username { top: 308px; }
  .field-password { top: 414px; }
  .forgot {
    position: absolute; left: 48px; top: 524px;
    display: flex; align-items: center; gap: 16px;
    font-size: 28px; color: var(--muted);
  }
  .checkbox {
    width: 40px; height: 40px;
    background: var(--white);
    border: 3px solid var(--green); border-radius: 3px;
  }
  .btn-login {
    position: absolute; left: 48px; top: 596px;
    width: 248px; height: 92px;
    background: var(--green); border-radius: 3px;
    display: flex; align-items: center; justify-content: center; gap: 12px;
    font-size: 34px; font-weight: 500; color: var(--white);
  }
  .btn-login svg { width: 30px; height: 26px; }
  .link-register {
    position: absolute; left: 332px; top: 620px;
    font-size: 34px; font-weight: 500; color: var(--green);
    padding-bottom: 4px;
    border-bottom: 3px solid var(--green);
  }
  .steps {
    position: absolute; left: 44px; right: 47px; top: 722px;
    border-top: 2px solid #cfd3d4;
    padding-top: 22px;
    text-align: center;
  }
  .steps-title {
    font-size: 22px; font-weight: 600; color: var(--ink);
    letter-spacing: 0.3px;
  }
  .steps-list {
    list-style: none;
    display: flex; justify-content: space-between;
    margin-top: 18px;
    font-size: 21px; font-weight: 500; color: var(--muted);
  }
  .steps-list b { color: var(--green); font-weight: 700; }
</style>
</head>
<body>
  <main class="screen">
    <div class="brand">
      <span class="brand-dot"></span>
      <span class="brand-name">brindle-oak</span>
    </div>

    <section class="pitch">
      <p class="pitch-headline">WANT TO EARN EXTRA MONEY?</p>
      <p class="pitch-sub">WITH BRINDLE-OAK.COM YOU CAN!</p>
    </section>

    <h1 class="login-title">Login</h1>
    <div class="field field-username">username</div>
    <div class="field field-password">password</div>

    <div class="forgot">
      <span class="checkbox"></span>
      <span>Forgot password?</span>
    </div>

    <div class="btn-login">
      Login
      <svg viewBox="0 0 30 26" aria-hidden="true">
        <path d="M3 4 L12 13 L3 22 M15 4 L24 13 L15 22" fill="none" stroke="#ffffff" stroke-width="5" stroke-linecap="round" stroke-linejoin="round"/>
      </svg>
    </div>
    <span class="link-register">Register</span>

    <section class="steps">
      <p class="steps-title">BRINDLE-OAK.COM. IT'S AS EASY AS 1, 2, 3.</p>
      <ol class="steps-list">
        <li><b>(1)</b> Register</li>
        <li><b>(2)</b> Earn &amp; Win Coins</li>
        <li><b>(3)</b> Redeem Coins</li>
      </ol>
    </section>
  </main>
</body>
</html>
```